Revise our Visual Graphic - CPA firm

We are a small specialty CPA firm that provides consulting services to companies in three areas: Information Security, Compliance & Attestation.

We need a tool to present our range of services and how they help our customers. We might use this on the website and when meeting face to face with clients to talk through what we do and how we can help.

I'm seeking a revised and updated graphic presentation image to explain our services. This graphic framework image will be one we can use on our website and use when we sell and explain our services to our clients. This graphic framework is meant to be a visual tool to make is easier to explain what we do to our clients.

We have a graphic that we like, but we don't LOVE IT yet. Your mission is you choose to accept it is to professionalize our graphic design. (see attached graphic)

The overall "environment" is represented by RISK, REGULATORY, REVENUE. These are the 3 reasons people would hire us. The bigger picture eco system.

The three overlapping circles show are three major service categories and inside the circles are lists of the specific services we can provide. We have overlapping circles to show that we can save them money and time if we provide more than one type of service.

The words on the dotted lines are what we commonly do on each project which is 3 things: IDENTIFY, EVALUATE, REPORT. These three things we do for all of our services so a faint circle with arrows or somehow showing a circular ongoing process would be good.

As you can see we are using one graphic to show many things and relationships.

The title of this graphic is "K7 Framework"

I look forward to your great ideas! Thanks.

Reason: Just to give a little more time after the weekend.

Target Market(s)

Presidents and Vice Presidents of small companies.

Industry/Entity Type

Graphic Design

Colors
faee3f
86cfc7
acd037
f68d4d

Requirements
Must have
• Be able to show this visual on one page of a website or PowerPoint presentation without scrolling down.

All of the written text on my draft example must be used and fit into the new design.
Nice to have
• When you design it think of how this can be used for both presentations, but also may be used on the website and people might click on different elements to learn more.

I picked some colors, but feel free to pick other colors. The only important thing to know is that the logo is black and yellow.

```html
<!DOCTYPE html>
<html lang="en">
<head>
<meta charset="utf-8">
<title>K7 Framework</title>
<link rel="stylesheet" href="https://fonts.googleapis.com/css2?family=Nunito:wght@800&family=Raleway:wght@400;500;700&family=Montserrat:wght@700&display=swap">
<style>
  :root {
    --bg: #f0f0f1;
    --sky-pale: #c3e3f6;
    --sky-mid: #acd8f2;
    --sky-deep: #97ceef;
    --sky-title: #bde0f6;
    --peach: #f5b28b;
    --leaf: #a6d28b;
    --ink: #555a60;
    --ink-strong: #5a5f66;
    --white: #ffffff;
    --beam: rgba(255,255,255,0.55);
  }
  * { margin: 0; padding: 0; box-sizing: border-box; }
  html, body { width: 1200px; height: 1000px; overflow: hidden; background: var(--bg); }
  .canvas { position: relative; width: 1200px; height: 1000px; }
  .title-pill {
    position: absolute; left: 57px; top: 93px; width: 343px; height: 57px;
    background: var(--sky-title); border-radius: 12px;
    display: flex; align-items: center; justify-content: center;
    font-family: "Nunito", sans-serif; font-weight: 800; font-size: 35px;
    color: var(--white); letter-spacing: 0.5px;
  }
  .diagram { position: absolute; left: 0; top: 0; }
  .corner-letter { font-family: "Montserrat", sans-serif; font-weight: 700; font-size: 27px; fill: var(--ink-strong); }
  .driver-label { font-family: "Raleway", sans-serif; font-weight: 500; font-size: 15px; fill: var(--ink); letter-spacing: 0.3px; }
  .category-label { font-family: "Raleway", sans-serif; font-weight: 400; font-size: 17px; fill: var(--ink); letter-spacing: 0.8px; }
  .service-item { font-family: "Raleway", sans-serif; font-weight: 400; font-size: 13px; fill: var(--ink); }
  .process-label { font-family: "Raleway", sans-serif; font-weight: 700; font-size: 21px; fill: var(--leaf); letter-spacing: 0.5px; }
  .firm-name { font-family: "Raleway", sans-serif; font-weight: 700; font-size: 20px; fill: var(--ink-strong); }
  .process-path { stroke: var(--leaf); stroke-width: 4; stroke-dasharray: 11 8; fill: none; }
  .process-node { fill: var(--leaf); }
  .service-ring { fill: var(--white); stroke: var(--peach); stroke-width: 19; }
</style>
</head>
<body>
<div class="canvas">
  <div class="title-pill">K7 Framework</div>

  <svg class="diagram" width="1200" height="1000" viewBox="0 0 1200 1000" aria-label="K7 Framework diagram">
    <defs>
      <linearGradient id="environment-fill" x1="0" y1="0" x2="0" y2="1">
        <stop offset="0" stop-color="var(--sky-mid)"/>
        <stop offset="0.5" stop-color="var(--sky-pale)"/>
        <stop offset="1" stop-color="var(--sky-deep)"/>
      </linearGradient>
    </defs>

    <!-- connecting beams from service circles -->
    <polygon points="300,290 470,370 420,492 300,460" fill="var(--beam)"/>
    <polygon points="900,290 730,370 780,492 900,460" fill="var(--beam)"/>
    <polygon points="535,692 665,692 665,790 535,790" fill="var(--beam)"/>

    <!-- environment triangle -->
    <polygon role="img" aria-label="Environment area: regulatory, risk and revenue drivers around the firm" points="600,225 285,692 915,692" fill="url(#environment-fill)"/>

    <text class="corner-letter" x="598" y="280" text-anchor="middle">R</text>
    <text class="corner-letter" x="323" y="684" text-anchor="middle">R</text>
    <text class="corner-letter" x="875" y="684" text-anchor="middle">R</text>
    <text class="driver-label" x="598" y="320" text-anchor="middle">REGULATORY</text>
    <text class="driver-label" x="368" y="672">RISK</text>
    <text class="driver-label" x="832" y="672" text-anchor="end">REVENUE</text>
    <text class="firm-name" x="600" y="502" text-anchor="middle">Northvale</text>

    <!-- process path -->
    <line class="process-path" x1="577" y1="222" x2="270" y2="678"/>
    <line class="process-path" x1="622" y1="222" x2="930" y2="678"/>
    <line class="process-path" x1="290" y1="715" x2="908" y2="715"/>
    <circle class="process-node" cx="577" cy="222" r="6"/>
    <circle class="process-node" cx="270" cy="678" r="6"/>
    <circle class="process-node" cx="622" cy="222" r="6"/>
    <circle class="process-node" cx="930" cy="678" r="6"/>
    <circle class="process-node" cx="290" cy="715" r="6"/>
    <circle class="process-node" cx="908" cy="715" r="6"/>
    <text class="process-label" x="445" y="251">IDENTIFY</text>
    <text class="process-label" x="925" y="653">EVALUATE</text>
    <text class="process-label" x="315" y="747">REPORT</text>

    <!-- compliance -->
    <circle class="service-ring" cx="291" cy="375" r="76"/>
    <text class="service-item" text-anchor="middle">
      <tspan x="291" y="342">CFPB</tspan>
      <tspan x="291" y="358">Readiness</tspan>
      <tspan x="291" y="374">FISMA</tspan>
      <tspan x="291" y="390">FedRamp</tspan>
      <tspan x="291" y="406">HITECH</tspan>
      <tspan x="291" y="422">HIPAA</tspan>
    </text>
    <text class="category-label" x="291" y="487" text-anchor="middle">COMPLIANCE</text>

    <!-- attestation -->
    <circle class="service-ring" cx="912" cy="375" r="76"/>
    <text class="service-item" text-anchor="middle">
      <tspan x="912" y="363">SSAE 16</tspan>
      <tspan x="912" y="379">WebTrust</tspan>
      <tspan x="912" y="395">SOC 2</tspan>
    </text>
    <text class="category-label" x="912" y="487" text-anchor="middle">ATTESTATION</text>

    <!-- information security -->
    <circle class="service-ring" cx="600" cy="830" r="76"/>
    <text class="service-item" text-anchor="middle">
      <tspan x="600" y="812">ISO 27001</tspan>
      <tspan x="600" y="828">PCI-DSS</tspan>
      <tspan x="600" y="844">Penetration Test</tspan>
    </text>
    <text class="category-label" x="600" y="935" text-anchor="middle">INFORMATION SECURITY</text>
  </svg>
</div>
</body>
</html>
```